Xmas banner Lathermoss handmade skincare

We need a xmas sale banner for our skincare website and a few different ones for instagram. Our website is www.lathermoss-example.com, you can use any of our products to include in the banner. We also have some nice product group pictures on our instagram.com/lathermoss_example. If you could include a christmassy message for example "its beginning to feel alot like christmas".

Target Market(s)

Women, 18-35, luxury, handmade natural shoppers

Requirements
Must have
• See our site and instagram. You have creative freedom.
Nice to have
• Try incorporating our products in imaginative ways, for example using bath bombs as Christmas tree baubles
Should not have
• Dont send anything if you think it will look out of place.

```html
<!DOCTYPE html>
<html lang="en">
<head>
<meta charset="utf-8">
<title>Lathermoss Christmas Banners</title>
<link rel="stylesheet" href="https://fonts.googleapis.com/css2?family=Great+Vibes&display=swap">
<style>
  :root {
    --board: #5f5f5f;
    --wall-light: #cdb8a8;
    --wall-mid: #a88f7d;
    --wall-dark: #5e4b40;
    --table-mid: #7a6157;
    --table-dark: #4f3c34;
    --ribbon-red: #b8283a;
    --box-gold: #b5a68a;
    --box-shade: #8f8068;
    --ink: #ffffff;
    --shadow: rgba(60, 40, 30, 0.55);
  }
  * { margin: 0; padding: 0; box-sizing: border-box; }
  html, body {
    width: 1200px;
    height: 1065px;
    overflow: hidden;
    background: var(--board);
  }
  .board { position: relative; width: 1200px; height: 1065px; }

  .banner { position: absolute; overflow: hidden; }
  .banner--wide { left: 83px; top: 79px; width: 1037px; height: 432px; }
  .banner--square { left: 83px; top: 624px; width: 361px; height: 360px; }

  .banner__backdrop {
    position: absolute; inset: 0;
    background:
      linear-gradient(to bottom, transparent 0 66%, var(--table-mid) 72%, var(--table-dark) 100%),
      linear-gradient(100deg, var(--wall-light) 0%, var(--wall-mid) 55%, var(--wall-dark) 100%);
  }
  .banner--square .banner__backdrop {
    background:
      linear-gradient(to bottom, transparent 0 76%, var(--table-mid) 81%, var(--table-dark) 100%),
      linear-gradient(100deg, var(--wall-light) 0%, var(--wall-mid) 60%, var(--wall-dark) 100%);
  }

  .banner__gift {
    position: absolute;
    border-radius: 6px;
    background: linear-gradient(120deg, var(--ribbon-red) 0%, var(--ribbon-red) 28%, var(--box-gold) 52%, var(--box-shade) 100%);
  }
  .banner--wide .banner__gift { left: 68px; top: 132px; width: 384px; height: 252px; }
  .banner--square .banner__gift { left: 38px; top: 188px; width: 211px; height: 137px; }

  .headline {
    position: absolute;
    font-family: "Great Vibes", cursive;
    color: var(--ink);
    font-weight: 400;
    white-space: nowrap;
    line-height: 1;
    text-shadow: 0 2px 6px var(--shadow);
  }
  .banner--wide .headline { font-size: 78px; }
  .banner--wide .headline--one { left: 438px; top: 58px; }
  .banner--wide .headline--two { left: 540px; top: 148px; }
  .banner--square .headline { font-size: 41px; }
  .banner--square .headline--one { left: 27px; top: 50px; }
  .banner--square .headline--two { left: 80px; top: 96px; }

  .brand {
    position: absolute;
    font-family: "Great Vibes", cursive;
    color: var(--ink);
    font-weight: 400;
    white-space: nowrap;
    line-height: 1;
  }
  .banner--wide .brand { left: 786px; top: 352px; font-size: 48px; }
  .banner--square .brand { left: 242px; top: 322px; font-size: 28px; }
</style>
</head>
<body>
  <main class="board">
    <section class="banner banner--wide">
      <div class="banner__backdrop"></div>
      <div class="banner__gift" role="img" aria-label="Photo: open kraft gift box tied with a red ribbon bow, filled with handmade soaps and bath bombs, on a wooden table"></div>
      <p class="headline headline--one">Its beginning to feel</p>
      <p class="headline headline--two">alot like Christmas!</p>
      <p class="brand">Lathermoss</p>
    </section>

    <section class="banner banner--square">
      <div class="banner__backdrop"></div>
      <div class="banner__gift" role="img" aria-label="Photo: open kraft gift box tied with a red ribbon bow, filled with handmade soaps and bath bombs, on a wooden table"></div>
      <p class="headline headline--one">Its beginning to feel</p>
      <p class="headline headline--two">alot like Christmas!</p>
      <p class="brand">Lathermoss</p>
    </section>
  </main>
</body>
</html>
```